Marlowvale Wholefoods web design

Go to marlowvalewholefoods.com.au an using the current layout create a design that will attract customers to this wholefood website.

You may suggest / make slight changes to the layout to create effective graphic design principles.

The LOGO design is TM already. So no changes there. Second logo attached is authorised for use and is a area branding LOGO.

Colours need to reflect health and wellbeing.

Don't want Medical style or New age.
Updates

Thank you for your submissions so far. I have sent them out to a trusty panel of friends to hear what they have to say. Some of you have done very well.

Reason: There are a few submissions outstanding. I will eliminate a few designs today and give feed back. Thankyou

Thank you for your submissions so far I will not be asking for more design submissions from other designers. The ones I have are under consideration and there are a few minor changes to each that may just bring out the one that is IT! The two designs I have narrowed it down to are very different in approach so please bear with me a couple more days. Thank you.

Target Market(s)

Whole food health concious people target market locally Home Delivery would be young Mums with restricted movement because of young children. Older people that are restricted transport users.

Busy commuters that leave our area for work and just want to relax on the weekend with their family and local bush walking or garden activities.

Industry/Entity Type

Graphic Design

Requirements
Should not have
• Medical or sterile hospital feel. New age or too alternative living feel.

```html
<!DOCTYPE html>
<html lang="en">
<head>
<meta charset="utf-8">
<title>Marlowvale Wholefoods</title>
<link href="https://fonts.googleapis.com/css2?family=Catamaran:wght@400;500;600;700&family=Open+Sans:wght@400;600;700&display=swap" rel="stylesheet">
<style>
:root{
  --green:#5a9a1c;
  --green-dark:#3f7010;
  --green-deep:#2f5a0a;
  --green-text:#5b9a12;
  --orange:#f08a12;
  --text:#444;
  --muted:#8a8a8a;
  --rule:#e2e2e2;
  --white:#fff;
  --social:#b9b9b9;
}
*{margin:0;padding:0;box-sizing:border-box}
html,body{width:807px;height:1200px;overflow:hidden;background:var(--white)}
body{position:relative;font-family:"Open Sans",Arial,sans-serif;color:var(--text)}
.abs{position:absolute}
a{color:inherit;text-decoration:none}

.social{left:86px;top:25px;display:flex;gap:4px}
.social span{width:16px;height:16px;border-radius:50%;background:var(--social)}
.btn{top:24px;height:20px;width:53px;font:600 8px/20px "Open Sans",sans-serif;color:var(--white);text-align:center;border-radius:2px}
.btn-login{left:613px;background:linear-gradient(#6fb020,#4f8d14)}
.btn-signup{left:668px;background:linear-gradient(#f9a21e,#ee8a0c)}

.nav{left:0;top:53px;width:807px;height:34px;background:linear-gradient(#67a624,#4c8813)}
.nav a{position:absolute;top:0;font:500 11.5px/36px "Catamaran",sans-serif;color:var(--white);letter-spacing:.2px}
.brand{left:330px;top:53px;width:148px;height:34px;display:flex;align-items:center;justify-content:center}
.brand-name{font:700 13px/1.05 "Catamaran",sans-serif;color:var(--white);text-align:center;text-transform:uppercase;letter-spacing:.5px}

.hero{left:0;top:87px;width:807px;height:300px;background:radial-gradient(ellipse at 30% 35%,#e9b48c 0%,#c9a266 18%,#a7c454 45%,#7fae2c 75%,#5f9420 100%)}
.hero-title{left:0;width:807px;top:206px;text-align:center;font:700 25px/1 "Catamaran",sans-serif;color:var(--white);text-shadow:0 1px 3px rgba(0,0,0,.25)}
.hero-sub{left:0;width:807px;top:245px;text-align:center;font:600 15px/1 "Catamaran",sans-serif;color:var(--white);text-shadow:0 1px 3px rgba(0,0,0,.25)}
.dots{left:386px;top:370px;display:flex;gap:2px}
.dots span{width:9px;height:9px;border-radius:50%;background:var(--white)}

.welcome{left:0;width:807px;top:410px;text-align:center;font:500 21px/1.2 "Catamaran",sans-serif;color:var(--orange)}
.lead{left:0;width:807px;top:441px;text-align:center;font-size:10.5px;color:#444}
.intro{left:90px;width:627px;top:460px;text-align:center;font-size:7.5px;line-height:14px;color:var(--muted)}

.card{top:511px;width:156px;height:182px;border:1px solid var(--rule);background:linear-gradient(#fff 70%,#f6f6f6)}
.card .pack{position:absolute;left:53px;top:24px;width:48px;height:56px;border-radius:3px}
.card h3{position:absolute;left:13px;top:91px;width:138px;font:500 11.5px/14px "Catamaran",sans-serif;color:var(--green-text)}
.card p{position:absolute;left:13px;top:126px;width:140px;font-size:7px;line-height:11px;color:var(--muted)}
.card .price{position:absolute;left:14px;top:152px;font:700 15.5px/1 "Open Sans",sans-serif;color:var(--orange);letter-spacing:-.5px}

.divider{left:82px;top:724px;width:648px;height:1px;background:var(--rule)}
.news-title{left:84px;top:752px;font:400 17.5px/1 "Catamaran",sans-serif;color:#333}
.news{width:210px;height:50px}
.news .thumb{position:absolute;left:0;top:0;width:48px;height:46px}
.news h4{position:absolute;left:57px;top:-1px;width:150px;font:500 9.5px/13px "Open Sans",sans-serif;color:var(--green-text)}
.news p{position:absolute;left:57px;top:13px;width:145px;font-size:7.2px;line-height:12.8px;color:var(--muted)}
.news.wide p{top:26px}

.footer{left:0;top:982px;width:807px;height:178px;background:linear-gradient(#5d9a1e,#386b0c)}
.footer-col{top:1010px}
.footer-col h5{font:500 12.5px/1 "Catamaran",sans-serif;color:var(--white);margin-bottom:9px}
.footer-col ul{list-style:none}
.footer-col li{font-size:8.5px;line-height:16px;color:#e7f1d8}
.footer-col.nohead{top:1031px}
.copyright-band{left:0;top:1160px;width:807px;height:40px;background:var(--green-deep)}
.copyright{left:89px;top:1175px;font-size:8.3px;color:#bcd3a0}
</style>
</head>
<body>

<header>
  <div class="abs social" aria-label="Social links"><span></span><span></span><span></span><span></span></div>
  <a class="abs btn btn-login" href="#">LOGIN</a>
  <a class="abs btn btn-signup" href="#">SIGN UP</a>

  <nav class="abs nav">
    <a href="#" style="left:107px">HOME</a>
    <a href="#" style="left:166px">ABOUT US</a>
    <a href="#" style="left:246px">PRODUCTS</a>
    <a href="#" style="left:508px">SHOP</a>
    <a href="#" style="left:565px">CATEGORY</a>
    <a href="#" style="left:648px">CONTACT US</a>
  </nav>
  <div class="abs brand">
    <span class="brand-name">Marlowvale<br>Wholefoods</span>
  </div>
</header>

<section>
  <div class="abs hero" role="img" aria-label="Smiling woman lying in sunlit grass holding a red apple"></div>
  <h1 class="abs hero-title">MARLOWVALE FOR A HEALTHY LIFESTYLE</h1>
  <p class="abs hero-sub">CLASS TACITI SOCIOSQU AD LITORA TORQUENT</p>
  <div class="abs dots"><span></span><span></span><span></span></div>
</section>

<section>
  <h2 class="abs welcome">Welcome to Our Website Mainpage</h2>
  <p class="abs lead">Vivamus porttitor libero a tempus libero lectus feugiat felis Morbi diam mauris viverra in gravida eu mattis in ante</p>
  <p class="abs intro">libero id ullamcorper nonummy nibh ligula pulvinar metus eget consectetuer augue nisi quis lacus Ut ac mi quis lacus Phasellus felis dolor scelerisque a tempus eget lobortis id libero Donec scelerisque leo ac risus Praesent sit amet est In dictum dolor eu dictum porttitor enim felis viverra mi eget luctus massa purus</p>

  <article class="abs card" style="left:82px">
    <div class="pack" role="img" aria-label="Packet of Singapore noodles" style="background:linear-gradient(#2a2a2a 30%,#c8352a 30%,#c8352a 80%,#2a2a2a 80%)"></div>
    <h3>Fernwick Pantry Singa-<br>pore Noodles</h3>
    <p>This nut butter has absolutely no addi-<br>tives. Just Australian Peanuts.</p>
    <span class="price">$3.30</span>
  </article>
  <article class="abs card" style="left:245px">
    <div class="pack" role="img" aria-label="Jar of peanut butter" style="left:66px;width:24px;border-radius:4px;background:linear-gradient(#2b3c6a 25%,#f0e2c8 25%,#d9642a 70%,#2b3c6a 70%)"></div>
    <h3>Fresh Ground Peanut<br>Butter 280g</h3>
    <p>This nut butter has absolutely no addi-<br>tives. Just Australian Peanuts.</p>
    <span class="price">$3.30</span>
  </article>
  <article class="abs card" style="left:409px">
    <div class="pack" role="img" aria-label="Packet of soba noodles" style="background:linear-gradient(#2a2a2a 30%,#b9c84a 30%,#b9c84a 80%,#2a2a2a 80%)"></div>
    <h3>Fernwick Pantry Organic<br>Soba Noodles</h3>
    <p>This nut butter has absolutely no addi-<br>tives. Just Australian Peanuts.</p>
    <span class="price">$3.30</span>
  </article>
  <article class="abs card" style="left:571px">
    <div class="pack" role="img" aria-label="Packet of udon noodles" style="background:linear-gradient(#2a2a2a 30%,#3a6aa8 30%,#3a6aa8 80%,#2a2a2a 80%)"></div>
    <h3>Fernwick Pantry Udon<br>Noodles</h3>
    <p>This nut butter has absolutely no addi-<br>tives. Just Australian Peanuts.</p>
    <span class="price">$3.30</span>
  </article>
</section>

<div class="abs divider"></div>

<section>
  <h2 class="abs news-title">LATEST NEWS</h2>

  <article class="abs news" style="left:82px;top:791px">
    <div class="thumb" role="img" aria-label="Woman eating a fresh salad" style="background:linear-gradient(135deg,#e8d8c8,#b88a6a 60%,#8aa84a)"></div>
    <h4>Suspendisse quam leo</h4>
    <p>Morbi porta libero id ullamcorper non-ummy nibh ligula pulvinar metus eget consectetuer augue nisi quis</p>
  </article>
  <article class="abs news" style="left:298px;top:791px">
    <div class="thumb" role="img" aria-label="Hands holding fresh herbs" style="background:linear-gradient(135deg,#cfd8c0,#6f9a3a 60%,#3f6a22)"></div>
    <h4>Donec scelerisque leo</h4>
    <p>Morbi porta libero id ullamcorper non-ummy nibh ligula pulvinar metus eget consectetuer augue nisi quis</p>
  </article>
  <article class="abs news wide" style="left:519px;top:791px">
    <div class="thumb" role="img" aria-label="Basket of fresh vegetables" style="background:linear-gradient(135deg,#4f7a2a,#c87a3a 55%,#3a5a1a)"></div>
    <h4>Morbi ornare gravida elit Integer congue augue</h4>
    <p>Morbi porta libero id ullamcorper non-ummy nibh ligula pulvinar metus .</p>
  </article>

  <article class="abs news" style="left:82px;top:873px">
    <div class="thumb" role="img" aria-label="Man holding a healthy meal" style="background:linear-gradient(135deg,#dfe3e6,#6a4a3a 55%,#e8e8e8)"></div>
    <h4>Suspendisse quam leo</h4>
    <p>Morbi porta libero id ullamcorper non-ummy nibh ligula pulvinar metus eget consectetuer augue nisi quis</p>
  </article>
  <article class="abs news" style="left:298px;top:873px">
    <div class="thumb" role="img" aria-label="Bowls of grains and salads" style="background:linear-gradient(135deg,#3a3a32,#c8b89a 50%,#6a7a4a)"></div>
    <h4>Donec scelerisque leo</h4>
    <p>Morbi porta libero id ullamcorper non-ummy nibh ligula pulvinar metus eget consectetuer augue nisi quis</p>
  </article>
  <article class="abs news wide" style="left:519px;top:873px">
    <div class="thumb" role="img" aria-label="Woman holding a green salad" style="background:linear-gradient(135deg,#f2ece6,#a8745a 55%,#7a9a4a)"></div>
    <h4>Morbi ornare gravida elit Integer congue augue</h4>
    <p>Morbi porta libero id ullamcorper non-ummy nibh ligula pulvinar metus .</p>
  </article>
</section>

<footer>
  <div class="abs footer"></div>
  <div class="abs footer-col" style="left:89px">
    <h5>ABOUT</h5>
    <ul><li>Why We Are</li><li>How we teach</li><li>About Us</li><li>Consulting</li></ul>
  </div>
  <div class="abs footer-col" style="left:207px">
    <h5>PRODUCTS</h5>
    <ul><li>Alternative goods</li><li>Dairy Free</li><li>Gluten Free</li><li>Grocery</li><li>Health Supplements</li></ul>
  </div>
  <div class="abs footer-col nohead" style="left:327px">
    <ul><li>Natural Grocer</li><li>Organic</li><li>Specials</li><li>Sugar Replacements</li><li>Vegan</li></ul>
  </div>
  <div class="abs footer-col" style="left:453px">
    <h5>CATEGORY</h5>
    <ul><li>Baking</li><li>Beans &amp; Peas</li><li>Candy &amp; Sweet Treats</li><li>Cereals &amp; Granolas</li><li>Coffee &amp; Tea</li><li>Dried Fruit</li></ul>
  </div>
  <div class="abs footer-col nohead" style="left:579px">
    <ul><li>Flour</li><li>Free Range Meat</li><li>Gluten Free Processed Meat</li><li>Grains</li><li>Muesli</li><li>NUTS</li></ul>
  </div>
  <div class="abs copyright-band"></div>
  <p class="abs copyright">© 2014 Company Name &nbsp;All right reserved &nbsp;Term of Use</p>
</footer>

</body>
</html>
```